Business Card Design

redesign of card and recreation of logo based on image provided. the business is located in new york so the Brooklyn Bridge figures prominently in the scheme. product should be very clean.

Industry/Entity Type

Real Estate

Contact Information for Business Card

Wendell Ortwick 318 Tamsin Street Brooklyn, New York 11409 wendell@qorvane.com Mobile: 917-555-0143

Colors
cadf82
1b1b1b
ffffff

Requirements
Nice to have
• Brooklyn Bridge

```html
<!DOCTYPE html>
<html lang="en">
<head>
<meta charset="utf-8">
<title>Qorvane Realty – Business Card</title>
<link rel="stylesheet" href="https://fonts.googleapis.com/css2?family=Open+Sans:wght@400;600;700&display=swap">
<style>
  :root {
    --ink: #1b1b1b;
    --paper: #ffffff;
    --sage: #cadf82;
    --sage-deep: #a9b96a;
    --backdrop: #e9e6e1;
  }
  * { margin: 0; padding: 0; box-sizing: border-box; }
  html, body { width: 1200px; height: 913px; overflow: hidden; }
  body {
    background: var(--backdrop);
    font-family: "Open Sans", Arial, sans-serif;
    color: var(--ink);
    position: relative;
  }
  .card {
    position: absolute;
    width: 510px;
    height: 292px;
    border-radius: 16px;
    overflow: hidden;
    box-shadow: 0 10px 30px rgba(0,0,0,0.18);
  }
  .card-front { left: 60px; top: 310px; background: var(--paper); }
  .card-back { left: 630px; top: 310px; background: var(--ink); }

  .front-band { position: absolute; inset: 0; }

  .brand {
    position: absolute;
    display: flex;
    align-items: center;
    gap: 9px;
    font-weight: 600;
    letter-spacing: 1px;
    text-transform: uppercase;
    white-space: nowrap;
  }
  .brand-mark { width: 10px; height: 10px; background: currentColor; flex: none; }
  .card-front .brand { left: 36px; top: 150px; font-size: 18px; color: var(--ink); }
  .card-back .brand { left: 50%; top: 50%; transform: translate(-50%, -50%); font-size: 30px; color: var(--sage); }

  .divider {
    position: absolute;
    left: 262px; top: 38px;
    width: 1px; height: 130px;
    background: var(--sage-deep);
  }
  .holder { position: absolute; left: 278px; top: 34px; }
  .holder-name { font-size: 19px; font-weight: 700; text-transform: uppercase; letter-spacing: 0.3px; white-space: nowrap; }
  .holder-title { font-size: 11px; font-weight: 600; color: var(--sage-deep); text-transform: uppercase; letter-spacing: 1px; margin-top: 2px; }

  .contacts { position: absolute; left: 278px; top: 92px; list-style: none; }
  .contacts li { display: flex; align-items: center; gap: 7px; font-size: 12.5px; line-height: 18px; white-space: nowrap; }
  .contacts svg { width: 11px; height: 11px; flex: none; }

  .address {
    position: absolute;
    right: 22px; bottom: 16px;
    color: var(--paper);
    font-size: 13px;
    letter-spacing: 0.3px;
    white-space: nowrap;
  }
</style>
</head>
<body>
  <section class="card card-front">
    <svg class="front-band" viewBox="0 0 510 292" width="510" height="292" aria-hidden="true">
      <path d="M0,292 L0,258 Q280,246 510,150 L510,292 Z" fill="var(--ink)"/>
      <path d="M0,250 Q280,238 510,142" fill="none" stroke="var(--sage-deep)" stroke-width="2"/>
    </svg>

    <div class="brand"><span class="brand-mark"></span>Qorvane Realty</div>

    <div class="divider"></div>
    <div class="holder">
      <div class="holder-name">Wendell Ortwick</div>
      <div class="holder-title">Broker</div>
    </div>

    <ul class="contacts">
      <li>
        <svg viewBox="0 0 12 12"><path d="M3 1 L5 3.5 L4 5 Q5 7 7 8 L8.5 7 L11 9 L10 11 Q4 11 1 2 Z" fill="none" stroke="var(--sage-deep)" stroke-width="1"/></svg>
        718-555-0162
      </li>
      <li>
        <svg viewBox="0 0 12 12"><rect x="3" y="0.5" width="6" height="11" rx="1" fill="none" stroke="var(--sage-deep)" stroke-width="1"/><circle cx="6" cy="9.5" r="0.7" fill="var(--sage-deep)"/></svg>
        917-555-0143
      </li>
      <li>
        <svg viewBox="0 0 12 12"><rect x="0.5" y="2.5" width="11" height="7" fill="none" stroke="var(--sage-deep)" stroke-width="1"/><path d="M0.5 2.5 L6 7 L11.5 2.5" fill="none" stroke="var(--sage-deep)" stroke-width="1"/></svg>
        wendell@qorvane.com
      </li>
      <li>
        <svg viewBox="0 0 12 12"><circle cx="6" cy="6" r="5.2" fill="none" stroke="var(--sage-deep)" stroke-width="1"/><path d="M1 6 H11 M6 1 Q3 6 6 11 M6 1 Q9 6 6 11" fill="none" stroke="var(--sage-deep)" stroke-width="0.8"/></svg>
        www.qorvane.com
      </li>
    </ul>

    <p class="address">318 Tamsin Street Brooklyn, New York 11409</p>
  </section>

  <section class="card card-back">
    <div class="brand"><span class="brand-mark"></span>Qorvane Realty</div>
  </section>
</body>
</html>
```